KeyBridge needs a modern business card

We are a modern conveyancing company and we need to appeal to the top (Multi-million dollar properties)and bottom on the property conveyancing market but our sweet spot is the middle of the market. I like professional with a hint of unconventional.

Target Market(s)

As above

Industry/Entity Type

Real Estate

Contact Information for Business Card

Back Of card:
thinking black with the logo and a tag line (I could be wrong about the black)
Tag line - Clear Advice, Confident Settlement

Front of Card:
Marissa Doyle (BBus (Finance) LLB)
Licensed Conveyancer
Email: marissa@keybridge.com.au

Key Bridge
ABN: 41 836 907
Suite 14, Level 3, 9 Harlow Avenue Westmead, NSW 2145
Phone: 1300 782 916

Sydney - Melbourne - Brisbane (Perhaps have this along the bottom of the card)

Requirements
Must have
• Sleek, modern and top end appeal (But approachable)
Should not have
• Not too cluttered

```html
<!DOCTYPE html>
<html lang="en">
<head>
<meta charset="utf-8">
<title>KeyBridge Business Card</title>
<link href="https://fonts.googleapis.com/css2?family=Roboto:wght@400;500;700&display=swap" rel="stylesheet">
<style>
  :root {
    --canvas: #a9a7a8;
    --card-dark: #2a2a2a;
    --card-light: #fbfbfb;
    --navy: #35587c;
    --sky: #2ec8f5;
    --lime: #8ccf2f;
    --ink: #1f1f1f;
    --white: #ffffff;
  }
  * { margin: 0; padding: 0; box-sizing: border-box; }
  html, body { width: 1200px; height: 1200px; overflow: hidden; }
  body {
    background: var(--canvas);
    font-family: "Roboto", Arial, sans-serif;
    position: relative;
  }
  .card { position: absolute; overflow: hidden; }

  /* Back of card */
  .card-back {
    left: 238px; top: 117px; width: 713px; height: 420px;
    background: var(--card-dark);
  }
  .back-brand {
    position: absolute; left: 0; right: 0; top: 262px;
    display: flex; justify-content: center; align-items: center; gap: 16px;
  }
  .back-brand .brand-square { width: 30px; height: 30px; background: var(--navy); }
  .back-brand .brand-name {
    color: var(--white); font-size: 48px; font-weight: 500; letter-spacing: -0.5px;
  }
  .tagline {
    position: absolute; left: 0; right: 0; top: 370px;
    display: flex; justify-content: center; align-items: center; gap: 14px;
    color: var(--white); font-size: 18px; letter-spacing: 0.2px;
  }
  .tagline .rule { width: 80px; height: 3px; }
  .tagline .rule-blue { background: linear-gradient(90deg, transparent, #1f8fe6 40%); }
  .tagline .rule-green { background: linear-gradient(90deg, var(--lime) 60%, transparent); }

  /* Front of card */
  .card-front {
    left: 231px; top: 644px; width: 712px; height: 417px;
    background: var(--card-light);
  }
  .person { position: absolute; left: 35px; top: 76px; color: var(--ink); }
  .person-name { color: var(--navy); font-size: 31px; font-weight: 700; line-height: 1; margin-bottom: 8px; }
  .person-role { font-size: 17px; line-height: 21px; }
  .front-brand {
    position: absolute; left: 332px; top: 82px;
    display: flex; align-items: center; gap: 18px;
  }
  .front-brand .brand-square { width: 40px; height: 40px; background: var(--navy); }
  .front-brand .brand-name { color: var(--ink); font-size: 48px; font-weight: 500; letter-spacing: -0.5px; }
  .contact-list { position: absolute; left: 339px; top: 198px; list-style: none; color: var(--ink); }
  .contact-list li { display: flex; align-items: center; gap: 16px; font-size: 18px; height: 26px; }
  .contact-list svg { width: 18px; height: 14px; }
  .address { position: absolute; left: 339px; top: 280px; font-size: 18px; line-height: 26px; color: var(--ink); font-style: normal; }
  .abn { position: absolute; left: 35px; top: 315px; font-size: 18px; color: var(--ink); }
  .footer-band { position: absolute; left: 0; bottom: 0; width: 712px; height: 54px; }
  .offices {
    position: absolute; left: 338px; bottom: 0; height: 54px;
    display: flex; align-items: center; color: var(--white); font-size: 18px;
  }
  .offices .sep { margin: 0 9px; }
</style>
</head>
<body>

<section class="card card-back" aria-label="Back of card">
  <div class="back-brand">
    <span class="brand-square"></span>
    <span class="brand-name">KeyBridge</span>
  </div>
  <p class="tagline">
    <span class="rule rule-blue"></span>
    <span>Clear Advice, Confident Settlement</span>
    <span class="rule rule-green"></span>
  </p>
</section>

<section class="card card-front" aria-label="Front of card">
  <div class="person">
    <h1 class="person-name">Marissa Doyle</h1>
    <p class="person-role">(BBus (Finance) LLB)</p>
    <p class="person-role">Licensed Conveyancer</p>
  </div>

  <div class="front-brand">
    <span class="brand-square"></span>
    <span class="brand-name">KeyBridge</span>
  </div>

  <ul class="contact-list">
    <li>
      <svg viewBox="0 0 18 14" aria-hidden="true"><path fill="#2a7fc4" d="M2 3c0-2 14-2 14 0v2h-4V3.5H6V5H2z M5 6h8l2 7H3z"/><circle cx="9" cy="9.5" r="2" fill="#fff"/></svg>
      <span>1300 782 916</span>
    </li>
    <li>
      <svg viewBox="0 0 18 14" aria-hidden="true"><rect x="1" y="2" width="16" height="10" fill="#7cc53a"/><path d="M1 2l8 6 8-6" fill="none" stroke="#fff" stroke-width="1.5"/></svg>
      <span>marissa@keybridge.com.au</span>
    </li>
    <li>
      <svg viewBox="0 0 18 14" aria-hidden="true"><circle cx="9" cy="7" r="6" fill="#a9d7f2"/><path d="M3 7h12M9 1v12M5 3.5h8M5 10.5h8" stroke="#fff" stroke-width="0.8" fill="none"/></svg>
      <span>www.keybridge.com.au</span>
    </li>
  </ul>

  <address class="address">Suite 14, Level 3, 9 Harlow Avenue<br>Westmead, NSW 2145</address>

  <p class="abn">ABN: 41 836 907</p>

  <svg class="footer-band" viewBox="0 0 712 54" aria-hidden="true">
    <polygon points="0,27 160,27 145,54 0,54" fill="var(--sky)"/>
    <polygon points="160,27 300,27 270,54 145,54" fill="var(--lime)"/>
    <polygon points="305,0 712,0 712,54 270,54" fill="var(--navy)"/>
  </svg>
  <p class="offices"><span>Sydney</span><span class="sep">|</span><span>Melbourne</span><span class="sep">|</span><span>Brisbane</span></p>
</section>

</body>
</html>
```